DELVANE ROOFING YARD SIGN

We need a yard sign to put in our customers' yards when we are roofing their home.
Delvane Roofing
468 Pettigrew Rd
Harlan Falls OK 74452
phone: 580-555-0148

Maybe some verbiage like "Your Hometown Roofing Experts"
or
"Family Owned Since 1956"

```html
<!DOCTYPE html>
<html lang="en">
<head>
<meta charset="utf-8">
<title>Delvane Roofing Yard Sign</title>
<link rel="stylesheet" href="https://fonts.googleapis.com/css2?family=Alegreya+Sans+SC:wght@800&family=Rokkitt:wght@600&display=swap">
<style>
  :root {
    --page: #d9d9d9;
    --wood-dark: #3a2318;
    --wood-mid: #5a3726;
    --wood-light: #6e4530;
    --cream: #fbf5dc;
    --ink-brown: #3b1a0e;
    --photo-sky: #b9c6cf;
    --photo-roof: #c2663f;
    --logo-ring: #8a8a8a;
  }
  * { margin: 0; padding: 0; box-sizing: border-box; }
  html, body {
    width: 1200px; height: 1174px; overflow: hidden;
    background: var(--page);
  }
  .sign {
    position: absolute; left: 40px; top: 423px;
    width: 1120px; height: 328px; overflow: hidden;
    background:
      repeating-linear-gradient(180deg, rgba(0,0,0,0) 0 38px, rgba(0,0,0,.18) 38px 40px),
      linear-gradient(100deg, var(--wood-mid), var(--wood-dark) 45%, var(--wood-light) 75%, var(--wood-dark));
    box-shadow: 0 14px 30px rgba(0,0,0,.35);
  }
  .sign-art { position: absolute; inset: 0; }
  .brand-title {
    position: absolute; left: 540px; width: 575px; top: 18px;
    text-align: center; white-space: nowrap;
    font-family: "Alegreya Sans SC", sans-serif; font-weight: 800;
    font-size: 68px; line-height: 1; color: var(--cream);
    letter-spacing: -1px;
  }
  .slogan-band {
    position: absolute; left: 535px; right: 0; top: 98px; height: 135px;
    background: var(--cream);
    box-shadow: inset 0 6px 0 var(--wood-dark), inset 0 -6px 0 var(--wood-dark);
  }
  .slogan-band::before, .slogan-band::after {
    content: ""; position: absolute; left: 0; right: 6px; height: 2px; background: var(--ink-brown);
  }
  .slogan-band::before { top: 14px; }
  .slogan-band::after { bottom: 14px; }
  .slogan {
    position: absolute; left: 0; right: 0; top: 19px;
    text-align: center; white-space: nowrap;
    font-family: "Alegreya Sans SC", sans-serif; font-weight: 800;
    font-size: 55px; line-height: 49px; color: var(--ink-brown);
    letter-spacing: -0.5px;
  }
  .contact {
    position: absolute; left: 540px; width: 575px; top: 248px;
    text-align: center; white-space: nowrap;
    font-family: "Rokkitt", serif; font-weight: 600;
    font-size: 28px; line-height: 30px; color: var(--cream);
  }
  .logo-name {
    position: absolute; left: 307px; top: 121px; width: 220px;
    text-align: center;
    font-family: "Alegreya Sans SC", sans-serif; font-weight: 800;
    font-size: 30px; line-height: 36px; color: var(--ink-brown);
  }
</style>
</head>
<body>
  <main class="sign">
    <svg class="sign-art" width="1120" height="328" viewBox="0 0 1120 328">
      <defs>
        <linearGradient id="photoTone" x1="0" y1="0" x2="0" y2="1">
          <stop offset="0" stop-color="var(--photo-sky)"/>
          <stop offset=".45" stop-color="#a9a196"/>
          <stop offset="1" stop-color="var(--photo-roof)"/>
        </linearGradient>
      </defs>
      <path class="accent-arc" d="M428 0 Q322 160 304 328 H336 Q350 160 462 0 Z" fill="var(--cream)"/>
      <path class="photo" role="img" aria-label="Photo of a roofer in a cap and green sweater laying clay roof tiles"
            d="M0 0 H420 Q316 160 298 328 H0 Z" fill="url(#photoTone)"/>
      <circle class="logo-disc" cx="417" cy="163" r="128" fill="#ffffff" stroke="var(--logo-ring)" stroke-width="4"/>
    </svg>

    <p class="logo-name">Delvane<br>Roofing</p>

    <h1 class="brand-title">DELVANE ROOFING</h1>

    <div class="slogan-band">
      <p class="slogan">YOUR HOMETOWN<br>ROOFING EXPERTS</p>
    </div>

    <p class="contact">468 Pettigrew Rd, Harlan Falls OK 74452<br>Phone: 580-555-0148</p>
  </main>
</body>
</html>
```